LedgaVue Business Card

We need a business card design using the attached logo. The company is a financial services company that provides a dashboard (chart based information) for Executives of small businesses to use to better manage their information. The design must be progressive, make good utilization of the logo and project stability and financial security.

Industry/Entity Type

Financial

```html
<!DOCTYPE html>
<html lang="en">
<head>
<meta charset="utf-8">
<title>LedgaVue Business Card</title>
<link href="https://fonts.googleapis.com/css2?family=Open+Sans:wght@400;600;700;800&display=swap" rel="stylesheet">
<style>
  :root {
    --bg: #ece8e3;
    --card-white: #ffffff;
    --ink: #1a1a1a;
    --black: #000000;
    --red: #a01c1f;
    --divider: #9a9a9a;
  }
  * { margin: 0; padding: 0; box-sizing: border-box; }
  html, body {
    width: 1193px;
    height: 1200px;
    overflow: hidden;
    background: var(--bg);
    font-family: "Open Sans", Arial, sans-serif;
  }
  .card {
    position: absolute;
    width: 952px;
    height: 547px;
    overflow: hidden;
  }
  .card-front {
    left: 209px;
    top: 46px;
    background: var(--card-white);
    border-radius: 28px;
    border: 1px solid #cfcfcf;
  }
  .card-back {
    left: 31px;
    top: 617px;
    background: var(--black);
    border-radius: 56px;
  }
  .brand {
    position: absolute;
    display: flex;
    align-items: center;
    gap: 22px;
  }
  .brand-front {
    left: 0;
    right: 0;
    top: 52px;
    justify-content: center;
  }
  .brand-square {
    width: 62px;
    height: 62px;
    background: var(--red);
  }
  .brand-name {
    font-weight: 800;
    color: var(--ink);
    font-size: 84px;
    letter-spacing: -1px;
    line-height: 1;
  }
  .identity {
    position: absolute;
    right: 480px;
    top: 280px;
    text-align: right;
    color: var(--ink);
  }
  .identity .person {
    font-size: 30px;
    font-weight: 600;
    line-height: 40px;
  }
  .identity .role {
    font-size: 23px;
    color: var(--red);
    line-height: 34px;
  }
  .identity .address {
    font-size: 22px;
    line-height: 32px;
  }
  .divider {
    position: absolute;
    left: 494px;
    top: 278px;
    width: 2px;
    height: 140px;
    background: var(--divider);
  }
  .contacts {
    position: absolute;
    left: 513px;
    top: 284px;
    list-style: none;
  }
  .contacts li {
    display: flex;
    align-items: center;
    gap: 12px;
    height: 48px;
    font-size: 23px;
    color: var(--ink);
  }
  .contacts svg { width: 22px; height: 22px; flex: none; }
  .band { position: absolute; left: 0; top: 0; width: 952px; height: 547px; }
  .url {
    position: absolute;
    color: #fff;
    font-weight: 600;
    letter-spacing: 3px;
  }
  .url-front {
    left: 565px;
    top: 486px;
    font-size: 29px;
  }
  .brand-back {
    left: 0;
    right: 0;
    top: 170px;
    justify-content: center;
  }
  .brand-back .brand-square { background: #fff; width: 90px; height: 90px; }
  .brand-back .brand-name { color: #fff; font-size: 112px; }
  .url-back {
    left: 0;
    right: 0;
    top: 444px;
    text-align: center;
    font-size: 31px;
  }
</style>
</head>
<body>
  <section class="card card-front">
    <div class="brand brand-front">
      <span class="brand-square"></span>
      <span class="brand-name">LedgaVue</span>
    </div>

    <div class="identity">
      <p class="person">Your Name</p>
      <p class="role">Title</p>
      <p class="address">Street Name, City Name</p>
      <p class="address">Zip Code-00000</p>
    </div>

    <span class="divider"></span>

    <ul class="contacts">
      <li>
        <svg viewBox="0 0 24 24" aria-hidden="true"><path fill="#a01c1f" d="M6.6 10.8c1.4 2.8 3.8 5.1 6.6 6.6l2.2-2.2c.3-.3.7-.4 1-.2 1.1.4 2.3.6 3.6.6.6 0 1 .4 1 1V20c0 .6-.4 1-1 1C10.6 21 3 13.4 3 4c0-.6.4-1 1-1h3.5c.6 0 1 .4 1 1 0 1.3.2 2.5.6 3.6.1.3 0 .7-.2 1z"/></svg>
        012-345-6789
      </li>
      <li>
        <svg viewBox="0 0 24 24" aria-hidden="true"><rect x="6" y="2" width="12" height="20" rx="2" fill="#a01c1f"/><rect x="8" y="5" width="8" height="9" fill="#fff"/><circle cx="12" cy="18" r="1.4" fill="#fff"/></svg>
        012-345-6789
      </li>
      <li>
        <svg viewBox="0 0 24 24" aria-hidden="true"><rect x="2" y="5" width="20" height="14" rx="1.5" fill="#a01c1f"/><path d="M2.5 6 12 13l9.5-7" stroke="#fff" stroke-width="1.8" fill="none"/></svg>
        info@ledgavue.com
      </li>
    </ul>

    <svg class="band" viewBox="0 0 952 547" aria-hidden="true">
      <polygon points="0,466 470,466 448,490 0,490" fill="var(--red)"/>
      <polygon points="0,500 447,500 485,466 952,466 952,547 0,547" fill="var(--black)"/>
    </svg>
    <p class="url url-front">www.ledgavue.com</p>
  </section>

  <section class="card card-back">
    <div class="brand brand-back">
      <span class="brand-square"></span>
      <span class="brand-name">LedgaVue</span>
    </div>
    <p class="url url-back">www.ledgavue.com</p>
  </section>
</body>
</html>
```